PLF Business Card Design

I am attaching my logo and want both a black and white modern, contemporary card for my business.

Below are the details I require on the cards and of course I would need to be able to change this.

Thanks

Rob

Robert K Ellison

Sales & Marketing Director

 

Vivid Panel Hub

PO Box 7319

Marlowgate

Wessbury

ME9 5QX

 

Tel +44 (0) 1579 618 203

Mobile: +44 (0) 7713 240 967

Fax: +44 (0) 1579 837 114

Email: rob@vividpanelhub.example

Website: www.vividpanelhub.example

 

 

Be part of a World full of imagination,

knowledge and inspiration

 

 

Derek Paxford

Editorial Director

 

Vivid Panel Hub

42 Harrow Gardens

Whitton

Middlesex

TW6 8RN

 

Tel: +44 (0) 208 517 3926

Mobile: +44 (0) 7832 205 671

Email: derek@vividpanelhub.example

 

 

knowledge and inspiration

This is the same font as used in the logo.......

Robert K Ellison

 

Vivid Panel Hub

PO Box 7319

Marlowgate

Wessbury

ME9 5QX

 

Tel +44 (0) 1579 618 203

Fax: +44 (0) 1579 837 114

 

 

Derek Paxford

Editorial Director

 

Vivid Panel Hub

42 Harrow Gardens

Whitton

Middlesex

TW6 8RN

 

Tel: +44 (0) 208 517 3926

Please add the following words to the back of the card and maybe add the logo to the back again.....

knowledge and inspiration

Robert K Ellison

 

Vivid Panel Hub

PO Box 7319

Marlowgate

Wessbury

ME9 5QX

 

Tel +44 (0) 1579 618 203

Fax: +44 (0) 1579 837 114

 

 

Derek Paxford

Editorial Director

 

Vivid Panel Hub

42 Harrow Gardens

Whitton

Middlesex

TW6 8RN

 

Tel: +44 (0) 208 517 3926

knowledge and inspiration

Target Market(s)

Wide Format printing, Screen Printing, Digital Printing, Textile Printing, Signage, Digital Signage, Exhibition Graphics, Digital Textiles and more

Industry/Entity Type

Publishing

Requirements
Must have
• I would like to use these words on the back of the card both for a full black card and white card.

"Be part of a World full of imagination, knowledge and inspiration"

```html
<!DOCTYPE html>
<html lang="en">
<head>
<meta charset="utf-8">
<title>Vivid Panel Hub business cards</title>
<link href="https://fonts.googleapis.com/css2?family=Tinos:wght@400;700&display=swap" rel="stylesheet">
<style>
:root{
  --backdrop:#4f5654;
  --card-white:#ffffff;
  --card-black:#000000;
  --brand-orange:#f7941d;
  --brand-blue:#1b9ad6;
  --name-blue:#1583c6;
  --band-blue-top:#1a7fd0;
  --band-blue-bottom:#0d5ea8;
  --band-warm-top:#fbb03b;
  --band-warm-bottom:#e8322a;
  --text-grey:#8a8a8a;
  --text-dark:#333333;
}
*{margin:0;padding:0;box-sizing:border-box}
html,body{width:1200px;height:1200px;overflow:hidden;background:var(--backdrop)}
body{position:relative;font-family:"Tinos","Times New Roman",serif}
.card{position:absolute;width:462px;height:282px;box-shadow:6px 8px 10px rgba(0,0,0,.55);overflow:hidden}
.card--white{background:var(--card-white);color:var(--text-grey)}
.card--black{background:var(--card-black);color:#fff}
.card--corner-tr{border-top-right-radius:64px}
.card--corner-bl{border-bottom-left-radius:64px}
.brand{position:absolute;display:flex;align-items:center;gap:10px}
.brand__dot{width:56px;height:56px;border-radius:50%;background:var(--brand-blue);flex:none}
.brand__name{font-size:27px;font-weight:700;color:var(--brand-orange);line-height:1}
.brand__tag{position:absolute;font-size:7px;line-height:9px;text-align:center;width:130px}
.quote{position:absolute;left:0;width:100%;text-align:center;font-size:15px;white-space:nowrap}
.person{position:absolute;text-align:center;width:200px}
.person__name{font-weight:700;font-size:14px;color:var(--name-blue)}
.person__name--large{font-size:18px}
.person__title{font-size:9.5px;margin-top:2px}
.contact{position:absolute;font-size:9.5px;line-height:14.6px;white-space:nowrap}
.band{position:absolute;bottom:0;height:29px}
.band--warm{left:0;width:54px;background:linear-gradient(var(--band-warm-top),var(--band-warm-bottom))}
.band--blue{left:65px;right:0;background:linear-gradient(var(--band-blue-top),var(--band-blue-bottom))}
.white-text{color:#fff}
.blue-text{color:var(--name-blue)}
.dark-text{color:var(--text-dark)}
</style>
</head>
<body>

<section class="card card--white card--corner-tr" style="left:49px;top:42px">
  <div class="brand" style="left:25px;top:26px"><span class="brand__dot"></span><span class="brand__name">Vivid Panel Hub</span></div>
  <div class="person" style="left:39px;top:174px"><div class="person__name">Robert K Ellison</div><div class="person__title">Sales &amp; Marketing Director</div></div>
  <div class="contact" style="left:284px;top:138px">PO Box 7319, Marlowgate,<br>Wessbury, ME9 5QX<br>Tel +44 (0) 1579 618 203<br>Mobile: +44 (0) 7713 240 967<br>Fax: +44 (0) 1579 837 114<br>Email: rob@vividpanelhub.example<br>Website: www.vividpanelhub.example</div>
  <div class="band band--warm"></div><div class="band band--blue"></div>
</section>

<section class="card card--black card--corner-tr" style="left:653px;top:50px">
  <div class="brand" style="left:25px;top:26px"><span class="brand__dot"></span><span class="brand__name">Vivid Panel Hub</span></div>
  <div class="brand__tag" style="left:85px;top:90px">Join a Hub full of colour, vision and bright ideas</div>
  <div class="quote" style="top:121px">" A Panel full of colour, creativity and bright connection"</div>
  <div class="person" style="left:38px;top:173px"><div class="person__name">Robert K Ellison</div><div class="person__title">Sales &amp; Marketing Director</div></div>
  <div class="contact" style="left:292px;top:145px;color:#bbb;line-height:15.6px">PO Box 7319, Marlowgate,<br>Wessbury, ME9 5QX<br>Tel +44 (0) 1579 618 203<br>Mobile: +44 (0) 7713 240 967<br>Fax: +44 (0) 1579 837 114<br>Email: rob@vividpanelhub.example<br>Website: www.vividpanelhub.example</div>
  <div class="band band--warm"></div><div class="band band--blue"></div>
</section>

<section class="card card--black card--corner-bl" style="left:50px;top:373px">
  <div class="brand" style="left:28px;top:40px"><span class="brand__dot"></span><span class="brand__name">Vivid Panel Hub</span></div>
  <div class="person" style="left:56px;top:205px"><div class="person__name person__name--large white-text">Derek Paxford</div><div class="person__title">Editorial Director</div></div>
  <div class="contact" style="left:290px;top:156px">PO Box 7319, Marlowgate,<br>Wessbury, ME9 5QX<br>Tel +44 (0) 1579 618 203<br>Mobile: +44 (0) 7713 240 967<br>Fax: +44 (0) 1579 837 114<br>Email: rob@vividpanelhub.example<br>Website: www.vividpanelhub.example</div>
</section>

<section class="card card--black card--corner-bl" style="left:653px;top:380px">
  <div class="brand" style="left:30px;top:40px"><span class="brand__dot"></span><span class="brand__name">Vivid Panel Hub</span></div>
  <div class="brand__tag" style="left:90px;top:105px">Join a Hub full of colour, vision and bright ideas</div>
  <div class="quote" style="top:144px">" A Panel full of colour, creativity and bright connection"</div>
  <div class="person" style="left:57px;top:206px"><div class="person__name person__name--large white-text">Derek Paxford</div><div class="person__title">Editorial Director</div></div>
  <div class="contact" style="left:287px;top:171px">PO Box 7319, Marlowgate,<br>Wessbury, ME9 5QX<br>Tel +44 (0) 1579 618 203<br>Mobile: +44 (0) 7713 240 967<br>Fax: +44 (0) 1579 837 114<br>Email: rob@vividpanelhub.example<br>Website: www.vividpanelhub.example</div>
</section>

<section class="card card--white card--corner-tr" style="left:67px;top:770px">
  <div class="brand" style="left:25px;top:26px"><span class="brand__dot"></span><span class="brand__name">Vivid Panel Hub</span></div>
  <div class="person" style="left:39px;top:174px"><div class="person__name">Robert K Ellison</div><div class="person__title">Sales &amp; Marketing Director</div></div>
  <div class="contact" style="left:289px;top:144px">PO Box 7319, Marlowgate,<br>Wessbury, ME9 5QX<br>Tel +44 (0) 1579 618 203<br>Mobile: +44 (0) 7713 240 967<br>Fax: +44 (0) 1579 837 114<br>Email: rob@vividpanelhub.example<br>Website: www.vividpanelhub.example</div>
  <div class="band band--warm"></div><div class="band band--blue"></div>
</section>

<section class="card card--white card--corner-bl" style="left:602px;top:775px">
  <div class="brand" style="left:28px;top:44px"><span class="brand__dot"></span><span class="brand__name">Vivid Panel Hub</span></div>
  <div class="brand__tag dark-text" style="left:94px;top:105px">Join a Hub full of colour, vision and bright ideas</div>
  <div class="quote dark-text" style="top:145px">" A Panel full of colour, creativity and bright connection"</div>
  <div class="person" style="left:55px;top:206px"><div class="person__name person__name--large">Derek Paxford</div><div class="person__title dark-text">Editorial Director</div></div>
  <div class="contact blue-text" style="left:286px;top:175px">PO Box 7319, Marlowgate,<br>Wessbury, ME9 5QX<br>Tel +44 (0) 1579 618 203<br>Mobile: +44 (0) 7713 240 967<br>Fax: +44 (0) 1579 837 114<br>Email: rob@vividpanelhub.example<br>Website: www.vividpanelhub.example</div>
</section>

</body>
</html>
```